Velvet Meadow Custom Handmade Designs and more needs new business card

I am looking to get a new design for my business cards. My business is based in Baltimore, MD. The company is called “Velvet Meadow”. We offers a variety of products and services. The products include handmade earrings, phone cases, picture frame, hats, tutu’s, ect. You name it we make it. As well as a lipstick line called “Jinxa”. We also are a independent consultant for Lorna Belt and Odette Brim. Lastly, we offer make up services from our certified MUA. I know it seems like a lot but it works. It’s all thinks girly. Our company tag lines are “You name it, we make it!” and “Everyday is a fashion show and the world id your runway… are you ready?”. I would like the business cards to have a girly appeal to it. I would like it to have some sample pictures of what we do if possible. I am open to different ideas. If you want to see what we have, you can view my website. MyVelvetMeadow.com …. its not finished but it will give you an idea of everything. I have attached my new designed logos. There are 3 different types that you can choose from. If you need pictures, let me know of what. Thanks!

Target Market(s)

Wide market women of all ages

Industry/Entity Type

Business

Contact Information for Business Card

Name: Velvet Meadow ; Website: MyVelvetMeadow.com ; Number: 555-204-1938 ; Email: MyVelvetMdw@mailnest.net ; IG: Velvet_Mdw Pagebook.net/VelvetMeadow14 ; Craftly.net/Shop/MyVelvetMeadow

Font styles to use
Serif
Sans Serif
Decorative
Script

Requirements
Must have
• One of the logos (but you can change the colors if you like)
Nice to have
• Location: Woodlawn, MD ; Owner/ designer: Bianca Thorne ; Taglines: You Name it, we make it and/or Every day is a fashion show and the world is your runway… Are you ready?

```html
<!DOCTYPE html>
<html lang="en">
<head>
<meta charset="utf-8">
<title>Velvet Meadow – Business Card</title>
<link href="https://fonts.googleapis.com/css2?family=Lato:wght@400;700&family=Dancing+Script:wght@600&display=swap" rel="stylesheet">
<style>
  :root {
    --page-bg: #3b3532;
    --card-bg: #151315;
    --pink: #e2197f;
    --violet: #a42fb2;
    --ink: #ececec;
    --ink-soft: #cfcfcf;
  }
  * { box-sizing: border-box; margin: 0; padding: 0; }
  html, body {
    width: 1200px; height: 844px; overflow: hidden;
    background: var(--page-bg);
    font-family: "Lato", Arial, sans-serif;
  }
  .sheet {
    width: 1200px; height: 844px;
    display: flex; align-items: center; justify-content: center; gap: 40px;
  }
  .card {
    width: 560px; height: 320px;
    background: var(--card-bg);
    border-radius: 4px;
    box-shadow: 0 10px 30px rgba(0,0,0,.45);
    position: relative;
    color: var(--ink);
  }

  /* Contact side */
  .brand-mark {
    position: absolute; left: 34px; top: 70px;
    width: 220px; height: 180px;
    display: flex; flex-direction: column; align-items: center; justify-content: center; gap: 14px;
  }
  .brand-mark .dot {
    width: 96px; height: 96px; border-radius: 50%;
    background: linear-gradient(135deg, var(--pink), var(--violet));
  }
  .brand-name {
    font-family: "Lato", Arial, sans-serif;
    font-weight: 700; font-size: 24px; color: var(--pink);
  }
  .contact {
    position: absolute; right: 34px; top: 38px;
    text-align: right; font-size: 16px; line-height: 1.38;
  }
  .owner-name {
    font-family: "Dancing Script", cursive;
    font-size: 26px; color: var(--pink); line-height: 1.1;
  }
  .owner-role { font-size: 16px; margin-bottom: 14px; }
  .label { color: var(--pink); }
  .contact .gap { height: 12px; }

  /* Services side */
  .brand-lockup {
    position: absolute; left: 50px; top: 52px; right: 40px;
    display: flex; align-items: center; gap: 18px;
  }
  .brand-lockup .dot {
    width: 70px; height: 70px; border-radius: 50%; flex: none;
    background: linear-gradient(135deg, var(--pink), var(--violet));
  }
  .brand-lockup .brand-name { font-size: 36px; }
  .tagline {
    font-size: 11px; font-style: italic; color: var(--ink); margin-top: 6px; line-height: 1.35;
  }
  .services {
    position: absolute; left: 0; right: 0; top: 180px;
    text-align: center; font-size: 17px; line-height: 1.5; color: var(--ink-soft);
  }
  .sep { color: var(--pink); margin: 0 6px; }
</style>
</head>
<body>
<main class="sheet">
  <section class="card card--contact">
    <div class="brand-mark">
      <span class="dot"></span>
      <span class="brand-name">Velvet Meadow</span>
    </div>
    <div class="contact">
      <p class="owner-name">Bianca Thorne</p>
      <p class="owner-role">Owner / Designer</p>
      <p><span class="label">T:</span> 555-204-1938</p>
      <p><span class="label">E:</span> MyVelvetMdw@mailnest.net</p>
      <p><span class="label">IG:</span> Velvet_Mdw</p>
      <p><span class="label">W:</span> MyVelvetMeadow.com</p>
      <div class="gap"></div>
      <p><span class="label">Pagebook.net</span>/VelvetMeadow14</p>
      <p><span class="label">Craftly.net</span>/Shop/MyVelvetMeadow</p>
    </div>
  </section>

  <section class="card card--services">
    <div class="brand-lockup">
      <span class="dot"></span>
      <div>
        <p class="brand-name">Velvet Meadow</p>
        <p class="tagline">Everyday is a fashion show and the world is your runway…<br>Are you ready?</p>
      </div>
    </div>
    <div class="services">
      <p>Bedazzled Items and Apparel<span class="sep">|</span>Handmade Earrings</p>
      <p>ID Tags<span class="sep">|</span>Custom Tutus<span class="sep">|</span>Jinxa Lipstick</p>
      <p>Certified MUA<span class="sep">|</span>Lorna Belt<span class="sep">|</span>Odette Brim</p>
    </div>
  </section>
</main>
</body>
</html>
```